Tatami Hall Sport promotional leaflet to attract new members

We are looking to produce a leaflet for a local judo club to attract seniors and juniors 5+ the leaflet needs to encourage people to attend classes and train in the martial art

Tatami Hall Sport are proud members of the KSB UK (mats for every) and practice traditional judo which mean we wear white Gi's to show cleanliness and tradition.

www.tatamihallsport.co.uk

Target Market(s)

Kids from 5+ and Adults

Font styles to use
Serif

Requirements
Must have
• Must include times of training and how to book onto a beginners induction
• it must look enticing and show that Judo is fun for all
• must highlight we open on Tuesdays and Thursdays
• Juniors are from 6.15pm to 7.15pm
• seniors 7.30pm to 9pm
• classes are held at Vantrel Gym, Unit 7, Marlow Row, Denholm Close, Halbrook, East Marlshire, HK4 2WD
• We practice on a Sprung floor Mat area and is great for men and women
• first two classes free
Nice to have
• Classes are run by an expeirnced team including
• Dan Merrow 5th Dan and international referee
• Luke Merrow 2nd Dan current Global Grappling Union European Champion

```html
<!DOCTYPE html>
<html lang="en">
<head>
<meta charset="utf-8">
<title>Train at Tatami Hall Sport</title>
<link rel="stylesheet" href="https://fonts.googleapis.com/css2?family=Montserrat:ital,wght@0,300;0,400;0,500;0,700;0,900;1,400&family=Oswald:wght@500;700&display=swap">
<style>
  :root {
    --ink: #0d0d0d;
    --red: #c0272d;
    --white: #ffffff;
    --soft: #cfcfcf;
    --grey-box: #5b5b5b;
  }
  * { box-sizing: border-box; margin: 0; padding: 0; }
  html, body { width: 934px; height: 1200px; overflow: hidden; background: var(--ink); }
  .leaflet {
    position: relative; width: 934px; height: 1200px; overflow: hidden;
    font-family: "Montserrat", Arial, sans-serif; color: var(--white);
    background: radial-gradient(ellipse at 50% 28%, #6a6a6a 0%, #3a3a3a 30%, #161616 62%, #080808 100%);
  }
  .hero-photo {
    position: absolute; left: 0; top: 0; width: 934px; height: 760px;
    background: radial-gradient(ellipse 340px 260px at 470px 300px, rgba(200,200,200,.35), rgba(0,0,0,0) 70%),
                linear-gradient(180deg, rgba(0,0,0,0) 60%, rgba(8,8,8,.9) 100%);
  }
  .deco { position: absolute; left: 0; top: 0; }
  .brand {
    position: absolute; top: 40px; left: 0; width: 100%;
    display: flex; align-items: center; justify-content: center; gap: 18px;
  }
  .brand-dot { width: 60px; height: 60px; border-radius: 50%; background: var(--red); }
  .brand-name { font-size: 52px; font-weight: 300; letter-spacing: 1px; color: var(--white); }
  .photo-diamond {
    position: absolute; width: 132px; height: 132px; transform: rotate(45deg);
    border: 6px solid var(--red); box-shadow: 0 0 0 2px rgba(0,0,0,.4);
  }
  .photo-left { left: 97px; top: 168px; background: linear-gradient(160deg, #8a8f96, #d9d9d9 55%, #9b6a6a); }
  .photo-right { left: 705px; top: 168px; background: linear-gradient(160deg, #cfd4d8, #8d9398 50%, #e6e6e6); }
  .headline {
    position: absolute; top: 300px; left: 0; width: 100%; text-align: center;
    font-weight: 900; line-height: .98; text-transform: uppercase;
    text-shadow: 6px 8px 0 rgba(60,60,60,.55);
  }
  .headline span { display: block; }
  .headline .l1 { font-size: 72px; }
  .headline .l2 { font-size: 58px; }
  .intro {
    position: absolute; top: 462px; left: 62px; width: 810px; text-align: center;
    font-size: 18px; line-height: 1.45; font-weight: 400;
  }
  .tag {
    position: absolute; height: 38px; background: var(--red);
    clip-path: polygon(10px 0, 100% 0, calc(100% - 10px) 100%, 0 100%);
    font-weight: 700; font-size: 18.5px; letter-spacing: .5px; line-height: 38px;
    padding-left: 20px; text-transform: uppercase;
  }
  .tag-tue { left: 42px; top: 570px; width: 250px; }
  .tag-thu { left: 42px; top: 790px; width: 262px; }
  .tag-induction { left: 358px; top: 570px; width: 302px; }
  .times { position: absolute; left: 57px; font-size: 15px; line-height: 1.28; }
  .times em { font-style: italic; }
  .times strong { font-weight: 700; display: block; margin-bottom: 7px; }
  .times-tue { top: 618px; }
  .times-thu { top: 840px; }
  .price {
    position: absolute; left: 232px; font-family: "Oswald", Arial, sans-serif;
    color: var(--red); text-transform: uppercase; font-weight: 700;
  }
  .price-tue { top: 624px; }
  .price-thu { top: 848px; }
  .price .label { font-size: 21px; line-height: .98; display: block; }
  .price .amount { font-size: 60px; line-height: .92; display: block; }
  .price .chevrons { font-family: "Montserrat", sans-serif; color: var(--white); font-size: 11px; letter-spacing: 1px; font-weight: 700; }
  .divider { position: absolute; left: 323px; width: 1px; background: var(--soft); }
  .divider-tue { top: 610px; height: 135px; }
  .divider-thu { top: 830px; height: 145px; }
  .dotted { position: absolute; left: 57px; width: 820px; border-top: 2px dotted #8c8c8c; }
  .induction-copy {
    position: absolute; left: 357px; top: 628px; width: 528px;
    font-size: 14.5px; line-height: 1.45; letter-spacing: .3px; color: var(--soft); font-weight: 400;
  }
  .feature-panel {
    position: absolute; left: 338px; top: 796px; width: 565px; height: 140px; background: var(--white);
    font-family: "Oswald", Arial, sans-serif; font-weight: 700; text-transform: uppercase;
    padding: 12px 0 0 16px; font-size: 24px; line-height: 1.15; color: var(--red);
  }
  .feature-panel .dark { color: var(--ink); }
  .photo-coach {
    position: absolute; left: 720px; top: 803px; width: 132px; height: 132px; transform: rotate(45deg);
    border: 5px solid var(--white); background: linear-gradient(150deg, #b7bcc2, #e8e8e8 50%, #7d8288);
  }
  .team {
    position: absolute; top: 992px; height: 100px; display: flex; align-items: center; justify-content: center;
    text-align: center; font-family: "Oswald", Arial, sans-serif; font-weight: 500;
    text-transform: uppercase; font-size: 19px; line-height: 1.25;
  }
  .team-intro { left: 80px; width: 250px; background: var(--red); clip-path: polygon(18px 0, 100% 0, 100% 100%, 0 100%, 0 18px); }
  .team-senior { left: 337px; width: 248px; background: var(--grey-box); }
  .team-champion { left: 593px; width: 250px; background: var(--red); clip-path: polygon(0 0, 100% 0, 100% calc(100% - 22px), calc(100% - 22px) 100%, 0 100%); }
  .address {
    position: absolute; top: 1126px; left: 0; width: 100%; text-align: center;
    font-size: 13.5px; font-weight: 700; letter-spacing: 1px; text-transform: uppercase;
  }
</style>
</head>
<body>
<main class="leaflet">
  <div class="hero-photo" role="img" aria-label="Soft-focus close-up of a judoka's clenched fist in a white gi"></div>

  <svg class="deco" width="934" height="1200" viewBox="0 0 934 1200" aria-hidden="true">
    <g fill="var(--white)">
      <polygon points="0,255 92,165 100,172 0,270"/>
      <polygon points="0,300 110,190 118,198 0,316"/>
      <polygon points="790,345 934,200 934,218 798,352"/>
      <polygon points="825,930 934,820 934,838 833,937"/>
      <polygon points="0,1120 70,1050 76,1056 0,1132"/>
    </g>
  </svg>

  <header class="brand">
    <div class="brand-dot"></div>
    <div class="brand-name">TATAMI HALL SPORT</div>
  </header>

  <div class="photo-diamond photo-left" role="img" aria-label="Group photo of club members in white gis lined up on the mat"></div>
  <div class="photo-diamond photo-right" role="img" aria-label="Judoka practising a throw on the mat during training"></div>

  <h1 class="headline"><span class="l1">Train at</span><span class="l2">Tatami Hall Sport</span></h1>

  <p class="intro">We normally train twice a week; both sessions are focused around improving and perfecting your Judo. We expect all of our Tatami Hall Sport members to be focused on developing their ability to become better at the art.</p>

  <div class="tag tag-tue">Tuesday Training</div>
  <div class="times times-tue">
    Juniors<br><em>(5 to 15 years old)</em><strong>6.15pm to 7.15pm</strong>
    Seniors<br><em>(16+ unless invited)</em><strong>7.30pm to 9pm</strong>
  </div>
  <div class="price price-tue"><span class="label">Session<br>Price</span><span class="amount">£5</span><span class="chevrons">&gt;&gt;&gt;&gt;&gt;&gt;&gt;&gt;&gt;</span></div>
  <div class="divider divider-tue"></div>

  <div class="tag tag-induction">Beginner’s Induction</div>
  <p class="induction-copy">The beginner’s induction will take place during the Tuesday sessions. This three-week program starts at the beginning of each month, once complete you will be able to attend both session’s as you will be deemed both safe to practice and have a level of skill to feel confident in practicing Randori.</p>

  <div class="dotted" style="top:760px"></div>

  <div class="tag tag-thu">Thursday Training</div>
  <div class="times times-thu">
    Juniors<br><em>(5 to 15 years old)</em><strong>6.15pm to 7.15pm</strong>
    Seniors<br><em>(16+ unless invited)</em><strong>7.30pm to 9pm</strong>
  </div>
  <div class="price price-thu"><span class="label">Session<br>Price</span><span class="amount">£5</span><span class="chevrons">&gt;&gt;&gt;&gt;&gt;&gt;&gt;&gt;&gt;</span></div>
  <div class="divider divider-thu"></div>

  <div class="feature-panel">
    We practice on a sprung<br>floor mat area and is<br>great for <span class="dark">men and women</span><br><span class="dark">first two classes free</span>
  </div>
  <div class="photo-coach" role="img" aria-label="Coach in a white gi standing with two junior judoka"></div>

  <div class="team team-intro">Classes are run<br>by an expeirnced<br>team including</div>
  <div class="team team-senior">Dan Merrow 5th Dan<br>and international<br>referee</div>
  <div class="team team-champion">Luke Merrow 2nd Dan current<br>Global Grappling Union<br>European Champion</div>

  <div class="dotted" style="top:1114px"></div>
  <p class="address">Vantrel Gym, Unit 7, Marlow Row, Denholm Close, Halbrook, East Marlshire, HK4 2WD</p>
  <div class="dotted" style="top:1170px"></div>
</main>
</body>
</html>
```